Business Card Design with new logo

Dorian Pelleway 4172
E 118th St Brenhollow, IL 62911
Cell: 217-555-0193
pellewayrestoration@mailvane.test

Classic Car Restoration Services Buy Sell Trade Consign

Dorian Pelleway 9698
Cell: 217-555-0193

```html
<!DOCTYPE html>
<html lang="en">
<head>
<meta charset="utf-8">
<title>Pelleway Restoration LLC – Business Card</title>
<link href="https://fonts.googleapis.com/css2?family=Lato:wght@400;700&family=Roboto:wght@500&display=swap" rel="stylesheet">
<style>
  :root {
    --bg: #2a2a2b;
    --card: #1d1d1e;
    --card-edge: #262627;
    --red: #e8302c;
    --white: #f4f4f4;
    --grey: #d9d9d9;
  }
  * { box-sizing: border-box; margin: 0; padding: 0; }
  html, body { width: 1200px; height: 900px; overflow: hidden; }
  body {
    background: var(--bg);
    font-family: "Lato", sans-serif;
    display: flex;
    flex-direction: column;
    align-items: center;
    justify-content: center;
    gap: 40px;
  }
  .card {
    width: 680px;
    height: 380px;
    background: linear-gradient(135deg, var(--card) 0%, var(--card-edge) 100%);
    box-shadow: 0 10px 30px rgba(0,0,0,.45);
    position: relative;
  }
  .brand {
    display: flex;
    align-items: center;
    gap: 12px;
  }
  .brand-dot {
    width: 30px; height: 30px;
    border-radius: 50%;
    background: var(--red);
    flex: none;
  }
  .brand-name {
    color: var(--white);
    font-family: "Lato", sans-serif;
    font-weight: 700;
    text-transform: uppercase;
    line-height: 1.2;
    white-space: nowrap;
  }
  .card-front {
    display: flex;
    align-items: center;
    justify-content: center;
  }
  .card-front .brand-dot { width: 34px; height: 34px; }
  .card-front .brand-name { font-size: 30px; letter-spacing: 2px; }
  .card-back {
    display: flex;
    align-items: center;
    padding: 0 30px;
  }
  .card-back .brand { width: 240px; flex: none; }
  .card-back .brand-name { font-size: 18px; letter-spacing: 1px; }
  .divider {
    width: 2px;
    height: 170px;
    background: var(--white);
    margin: 0 24px;
    flex: none;
  }
  .contact { color: var(--white); white-space: nowrap; }
  .person-name {
    font-family: "Roboto", sans-serif;
    font-weight: 500;
    color: var(--red);
    font-size: 30px;
    letter-spacing: .5px;
    text-transform: uppercase;
    line-height: 1;
  }
  .person-role { font-size: 16px; color: var(--grey); margin: 4px 0 14px; }
  .address { font-size: 17px; line-height: 1.3; margin-bottom: 12px; }
  .contact-list { list-style: none; font-size: 17px; line-height: 1.45; }
  .contact-list li { display: flex; align-items: center; gap: 10px; }
  .contact-list svg { width: 12px; height: 12px; flex: none; }
</style>
</head>
<body>
  <section class="card card-front">
    <div class="brand">
      <span class="brand-dot"></span>
      <span class="brand-name">Pelleway Restoration LLC</span>
    </div>
  </section>

  <section class="card card-back">
    <div class="brand">
      <span class="brand-dot"></span>
      <span class="brand-name">Pelleway<br>Restoration LLC</span>
    </div>
    <div class="divider"></div>
    <div class="contact">
      <h1 class="person-name">Renata Colwell</h1>
      <p class="person-role">Director</p>
      <p class="address">Dorian Pelleway 4172<br>E 118th St Brenhollow, IL 62911</p>
      <ul class="contact-list">
        <li>
          <svg viewBox="0 0 12 12"><path d="M3 1 L5 3.5 L4 5 Q5 7 7 8 L8.5 7 L11 9 L9.5 11 Q4 10.5 1 3 Z" fill="var(--red)"/></svg>
          217-555-0193
        </li>
        <li>
          <svg viewBox="0 0 12 12"><rect x="1" y="2.5" width="10" height="7" fill="none" stroke="var(--red)" stroke-width="1.2"/><path d="M1 2.5 L6 6.5 L11 2.5" fill="none" stroke="var(--red)" stroke-width="1.2"/></svg>
          pellewayrestoration@mailvane.test
        </li>
        <li>
          <svg viewBox="0 0 12 12"><circle cx="6" cy="6" r="5" fill="none" stroke="var(--red)" stroke-width="1.1"/><ellipse cx="6" cy="6" rx="2.2" ry="5" fill="none" stroke="var(--red)" stroke-width="1"/><path d="M1 6 H11" stroke="var(--red)" stroke-width="1"/></svg>
          www.pellewayrestoration.test
        </li>
      </ul>
    </div>
  </section>
</body>
</html>
```